Label for honey jars and buckets

My mom needs a label for her honey. The company is called 'Cedar Brook Apiary' It needs to say 'Raw Fireweed Honey' somewhere on the label and then in small print Terrace, BC with this phone number underneath 250-418-7364. There needs to be 3 sizes of the same label the 1) width 2 inches x height 2 3/4 inches 2) width 5 inches x height 3 inches 3) 2 3/4 inches round label

She really liked the first bee and honeycomb logo you did for my lotion label, the one with the white bee and yellow honeycomb, so something like that would be great. I've uploaded a few pictures of her bees and a picture of the fireweed flower that the bees make the honey from to give you some ideas.

It needs to have an artisan feel, it is a small company that's locally owned and operated.
Updates

I was thinking that having some mountain ranges worked into the background of the label would look nice and be really fitting, the picture of the fireweed that I uploaded has a good example of the types on mountains in the area. 

Industry/Entity Type

It Company

Requirements
Should not have
• Not too many colours

```html
<!DOCTYPE html>
<html lang="en">
<head>
<meta charset="utf-8">
<title>Cedar Brook Apiary – Round Honey Labels</title>
<link href="https://fonts.googleapis.com/css2?family=Arvo:wght@400;700&display=swap" rel="stylesheet">
<style>
  :root {
    --brown: #3b1f10;
    --orange: #f39a1e;
    --yellow: #fcc51c;
    --gold-ring: #f6c21a;
    --sky: #8ec6ec;
    --paper: #ffffff;
  }
  html, body {
    margin: 0;
    padding: 0;
    width: 1200px;
    height: 1000px;
    overflow: hidden;
    background: var(--paper);
  }
  .canvas {
    width: 1200px;
    height: 1000px;
    display: flex;
    align-items: center;
    justify-content: center;
    gap: 40px;
  }
  .label {
    width: 340px;
    height: 340px;
    display: block;
  }
  .rim { fill: var(--brown); }
  .gold-band { fill: var(--gold-ring); }
  .face-orange { fill: var(--orange); }
  .face-yellow { fill: var(--yellow); }
  .face-sky { fill: var(--sky); }
  .inner-line {
    fill: none;
    stroke: var(--brown);
    stroke-width: 2.5;
  }
  .brand-mark { fill: var(--brown); }
  .arc-title {
    font-family: "Arvo", Georgia, serif;
    font-weight: 700;
    font-size: 22px;
    letter-spacing: 2px;
    fill: var(--brown);
  }
  .brand-name {
    font-family: "Arvo", Georgia, serif;
    font-weight: 700;
    font-size: 27px;
    fill: var(--brown);
  }
  .small-print {
    font-family: "Arvo", Georgia, serif;
    font-weight: 400;
    font-size: 13px;
    letter-spacing: 0.5px;
    fill: var(--brown);
  }
</style>
</head>
<body>
<main class="canvas">

  <svg class="label label--orange" viewBox="0 0 340 340" aria-label="Round label, orange">
    <defs>
      <path id="arc-orange" d="M 58,172 A 112,112 0 0 1 282,172"/>
    </defs>
    <circle class="rim" cx="170" cy="170" r="168"/>
    <circle class="face-orange" cx="170" cy="170" r="158"/>
    <circle class="inner-line" cx="170" cy="170" r="146"/>
    <circle class="inner-line" cx="170" cy="170" r="140"/>
    <text class="arc-title"><textPath href="#arc-orange" startOffset="50%" text-anchor="middle">RAW FIREWEED HONEY</textPath></text>
    <circle class="brand-mark" cx="170" cy="136" r="24"/>
    <text class="brand-name" x="170" y="198" text-anchor="middle">Cedar Brook</text>
    <text class="brand-name" x="170" y="230" text-anchor="middle">Apiary</text>
    <text class="small-print" x="170" y="260" text-anchor="middle">Terrace, BC</text>
    <text class="small-print" x="170" y="279" text-anchor="middle">250-418-7364</text>
  </svg>

  <svg class="label label--yellow" viewBox="0 0 340 340" aria-label="Round label, yellow">
    <defs>
      <path id="arc-yellow" d="M 58,172 A 112,112 0 0 1 282,172"/>
    </defs>
    <circle class="rim" cx="170" cy="170" r="168"/>
    <circle class="face-yellow" cx="170" cy="170" r="163"/>
    <circle class="inner-line" cx="170" cy="170" r="146"/>
    <circle class="inner-line" cx="170" cy="170" r="140"/>
    <text class="arc-title"><textPath href="#arc-yellow" startOffset="50%" text-anchor="middle">RAW FIREWEED HONEY</textPath></text>
    <circle class="brand-mark" cx="170" cy="136" r="24"/>
    <text class="brand-name" x="170" y="198" text-anchor="middle">Cedar Brook</text>
    <text class="brand-name" x="170" y="230" text-anchor="middle">Apiary</text>
    <text class="small-print" x="170" y="260" text-anchor="middle">Terrace, BC</text>
    <text class="small-print" x="170" y="279" text-anchor="middle">250-418-7364</text>
  </svg>

  <svg class="label label--sky" viewBox="0 0 340 340" aria-label="Round label, sky blue">
    <defs>
      <path id="arc-sky" d="M 58,172 A 112,112 0 0 1 282,172"/>
    </defs>
    <circle class="rim" cx="170" cy="170" r="168"/>
    <circle class="gold-band" cx="170" cy="170" r="160"/>
    <circle class="face-sky" cx="170" cy="170" r="148"/>
    <circle class="inner-line" cx="170" cy="170" r="140"/>
    <text class="arc-title"><textPath href="#arc-sky" startOffset="50%" text-anchor="middle">RAW FIREWEED HONEY</textPath></text>
    <circle class="brand-mark" cx="170" cy="136" r="24"/>
    <text class="brand-name" x="170" y="198" text-anchor="middle">Cedar Brook</text>
    <text class="brand-name" x="170" y="230" text-anchor="middle">Apiary</text>
    <text class="small-print" x="170" y="260" text-anchor="middle">Terrace, BC</text>
    <text class="small-print" x="170" y="279" text-anchor="middle">250-418-7364</text>
  </svg>

</main>
</body>
</html>
```